載内容詳細に関しては、別添のExcel資料を参照してください。

・ターゲット
BtoB
建設業の方で掘削の作業でお悩みのある方
→既存の建設現場が想像以上に地盤が固く、掘れないなど

くい打ち機をお探しの方
→金額が高いため、中古の需要が高い

・カラーイメージ

▼参考
https://www.torimo-haruka.jp/

・デザイン、ムード
見る方が50代~60第と年配の方が予想されるため、明朝体を使用し、堅めでしっかりした企業のイメージでデザインお願いします

▼参考
https://www.hoshinue-koki.com/

【素材】
▼ソラノハコ便
https://7.soranohako.jp/2811-a47f09c3b5e1d2886f04c71a9e5b2d03f

配置やデザイン等はアレンジしていただいて構いません。
また、縦に制限はありません。

レスポンシブデザインのサイトで、bootstrap4を利用しコーディングする予定になります。

デザイン幅は2000px、コンテンツの幅はbootstrap4デフォルトのの1110pxを基準としてください。
ただし、最近のデザインの流行を取りいれて、フルワイドや、1200~1500px程度の幅のコンテンツをバランスよくレイアウトしてください。
コンテンツ配置は基本12分割になります。がデザインによっては、多少逸脱してもかまいません。
bootstrap4、12分割グリッドの基準のPSDも資料として添付しております。
ご参考になさってください。

本分のフォントはゴシック系は游ゴシック、メイリオ、明朝系は遊明朝でお願いします。
飾り文字はフリーフォントか、googleフォントを利用してください。

メイン画像部分・グローバルメニューは、ワイド適用でお願いします。

不明点、質問などありましたらメッセージ等でご連絡ください。
1ページ
青系
• 高解像度JPG (.jpg)
• フォトショップ形式 (.psd)
・資料上はサイト名(社名)や住所などは伏字にしております。
ご提案時点ではそのまま作成をお願いします。

・使用画像は当選後こちらで用意します。
ご提案時点では前項同様に、カンプデータ等をご使用のうえ、当選後に本内容へ差し替え修正をお願いします。
また、雰囲気が合っていれば、指定外の画像を追加掲載いただいてOKです。

・当選前提となった方は正式な社名及び連絡先をお伝えしますので修正対応をお願いします。
また希望の際は、当選後、中ページの制作及びコーディングも別途ご依頼可能です。

```html
<!DOCTYPE html>
<html lang="ja">
<head>
<meta charset="utf-8">
<title>株式会社○○○○</title>
<link rel="stylesheet" href="https://fonts.googleapis.com/css2?family=Noto+Serif+JP:wght@400;600;700&family=Noto+Sans+JP:wght@400;500;700&family=Cormorant+Garamond:wght@500;600&display=swap">
<style>
:root{
  --navy:#1c2f57;
  --blue:#1f4fa6;
  --blue-deep:#173f8a;
  --ink:#2a2f3a;
  --muted:#6d7380;
  --pale:#eef1f6;
  --faint:#e7ebf2;
  --grey:#9a9a9a;
  --white:#fff;
}
*{margin:0;padding:0;box-sizing:border-box}
html,body{width:1200px;height:2716px;overflow:hidden}
body{font-family:"Noto Serif JP",serif;color:var(--ink);background:var(--white);position:relative}
.sans{font-family:"Noto Sans JP",sans-serif}

/* header */
.site-header{position:absolute;top:0;left:0;width:1200px;height:56px;display:flex;align-items:center;justify-content:space-between;padding:0 0 0 20px;background:rgba(255,255,255,.96);z-index:3}
.brand{font-size:17px;font-weight:700;letter-spacing:.04em}
.gnav{display:flex;align-items:center;height:100%}
.gnav a{font-size:13px;color:var(--ink);text-decoration:none;margin-right:34px;font-family:"Noto Sans JP",sans-serif}
.gnav .nav-contact{margin:0;height:100%;width:170px;background:var(--blue);color:#fff;display:flex;align-items:center;justify-content:center;gap:8px}

/* hero */
.hero{position:absolute;top:0;left:0;width:1200px;height:572px}
.hero-photo{position:absolute;inset:0;background:linear-gradient(120deg,#1d2a3b 0%,#3b4a5c 35%,#55616d 60%,#2b3542 100%)}
.hero-photo::after{content:"";position:absolute;inset:0;background:linear-gradient(90deg,rgba(10,20,40,.55),rgba(10,20,40,.15))}
.hero-copy{position:absolute;left:116px;top:262px;color:#fff;z-index:2}
.hero-copy p{font-weight:700;line-height:1.35;letter-spacing:.03em}
.hero-copy .l1{font-size:44px}
.hero-copy .l2{font-size:52px;margin-top:14px}
.hero-copy small{font-size:26px;font-weight:600}
.hero-band{position:absolute;left:0;top:420px;width:860px;height:66px;background:var(--blue);color:#fff;display:flex;align-items:center;padding-left:116px;font-size:22px;font-weight:600;z-index:2}
.hero-band b{font-size:28px}

/* shared */
.sec-title{font-size:34px;font-weight:600;letter-spacing:.08em}
.sec-sub{font-family:"Cormorant Garamond",serif;font-size:13px;letter-spacing:.25em;color:var(--blue)}
.ghost{position:absolute;font-family:"Cormorant Garamond",serif;font-weight:500;color:var(--faint);letter-spacing:.05em;line-height:1;white-space:nowrap}
.btn{display:inline-flex;align-items:center;justify-content:space-between;background:var(--blue);color:#fff;font-size:13px;text-decoration:none;padding:0 22px;height:46px;font-family:"Noto Sans JP",sans-serif}
.btn svg{margin-left:18px}

/* company */
.company{position:absolute;top:572px;left:0;width:1200px;height:668px}
.company .ghost{right:-20px;top:84px;font-size:130px}
.company-photo{position:absolute;left:140px;top:56px;width:280px;height:492px;background:linear-gradient(160deg,#1a2438,#3a5a86 55%,#c7d3e6)}
.company-body{position:absolute;left:600px;top:104px;width:480px}
.company-body .sec-title{font-size:32px}
.company-body .lead{font-size:14px;line-height:2;margin-top:30px}
.company-body .text{font-size:12px;line-height:2;margin-top:24px;color:var(--muted)}
.company-body .btn{margin-top:44px;width:240px}

/* service */
.service{position:absolute;top:1240px;left:0;width:1200px;height:480px}
.service .ghost{left:356px;top:40px;font-size:90px}
.service-head{position:absolute;top:92px;width:100%;text-align:center}
.service-panels{position:absolute;top:180px;left:0;width:1200px;height:300px;display:flex}
.panel{position:relative;flex:1;color:#fff;overflow:hidden}
.panel-photo{position:absolute;inset:0}
.panel-1 .panel-photo{background:linear-gradient(135deg,#2d4e86,#4f6f9e 50%,#25406e)}
.panel-2 .panel-photo{background:linear-gradient(135deg,#3b5c8e,#6d86ad 50%,#2c4a7a)}
.panel-body{position:absolute;inset:0;display:flex;flex-direction:column;align-items:center;padding-top:60px;text-align:center}
.panel-body h3{font-size:30px;font-weight:600;letter-spacing:.06em}
.panel-body .sec-sub{color:#fff;margin-top:2px}
.panel-body p{font-size:13px;line-height:1.9;margin-top:16px}
.panel-body .btn{margin-top:22px;width:170px;height:38px;font-size:12px;background:rgba(31,79,166,.85)}

/* products */
.products{position:absolute;top:1720px;left:0;width:1200px;height:500px}
.products .ghost{left:20px;top:40px;font-size:110px;color:#f1f3f7}
.products-head{position:absolute;top:76px;width:100%;text-align:center}
.product-list{position:absolute;top:180px;left:268px;display:flex;gap:20px}
.product{width:152px;text-align:center}
.product-photo{width:152px;height:148px;background:var(--grey)}
.product span{display:block;font-size:13px;margin-top:28px;font-family:"Noto Sans JP",sans-serif}
.products .btn{position:absolute;left:480px;top:392px;width:240px}

/* contact */
.contact{position:absolute;top:2220px;left:0;width:1200px;height:328px;background:var(--pale)}
.contact .ghost{left:130px;top:28px;font-size:110px;color:#e2e7f0}
.contact-head{position:absolute;top:70px;width:100%;text-align:center}
.contact-note{position:absolute;top:146px;width:100%;text-align:center;font-size:13px;font-family:"Noto Sans JP",sans-serif}
.contact-row{position:absolute;top:214px;left:272px;display:flex;align-items:center;gap:62px}
.tel{display:flex;align-items:center;gap:12px;font-family:"Noto Sans JP",sans-serif;font-weight:700;font-size:36px;color:var(--blue-deep);letter-spacing:.02em}
.contact .btn{width:270px;height:60px;font-size:15px;justify-content:center;gap:12px}
.contact .btn svg{margin:0}

/* footer */
.site-footer{position:absolute;top:2548px;left:0;width:1200px;height:168px;background:var(--navy);color:#fff;font-family:"Noto Sans JP",sans-serif}
.site-footer .brand{position:absolute;left:268px;top:40px;font-family:"Noto Serif JP",serif;font-size:19px}
.f-address{position:absolute;left:268px;top:90px;font-size:11px;line-height:1.9;opacity:.85}
.f-nav{position:absolute;left:660px;top:44px;display:flex;gap:26px;font-size:12px}
.copy{position:absolute;left:820px;top:110px;font-size:10px;opacity:.7}
</style>
</head>
<body>

<section class="hero">
  <div class="hero-photo" role="img" aria-label="工場で溶接作業を行う作業員の写真"></div>
  <div class="hero-copy">
    <p class="l1">掘削製品<small>の設計・制作・改造、</small></p>
    <p class="l2">くい打ち機<small>の中古販売</small></p>
  </div>
  <div class="hero-band">創業より30年、<b>お客様の要望をカタチに</b>してきました。</div>
</section>

<header class="site-header">
  <div class="brand">株式会社○○○○</div>
  <nav class="gnav">
    <a href="#">ホーム</a><a href="#">事業内容</a><a href="#">製品紹介</a><a href="#">会社概要</a>
    <a class="nav-contact" href="#">
      <svg width="16" height="12" viewBox="0 0 16 12"><rect x=".5" y=".5" width="15" height="11" fill="none" stroke="#fff"/><path d="M1 1l7 6 7-6" fill="none" stroke="#fff"/></svg>お問い合わせ
    </a>
  </nav>
</header>

<section class="company">
  <div class="ghost">COMPANY</div>
  <div class="company-photo" role="img" aria-label="火花を散らして溶接する作業員の写真"></div>
  <div class="company-body">
    <h2 class="sec-title">会社概要</h2>
    <div class="sec-sub">COMPANY</div>
    <p class="lead">1990年の創業以来、お客様のご要望に応えた掘削、<br>高品質な掘削製品を提供しています。</p>
    <p class="text">確かな技術と経験を生かし、現場ごとの課題に合わせた製品づくりを行っています。<br>設計から制作、改造まで一貫して対応し、安心してお使いいただける品質をお届けします。<br>中古くい打ち機の販売も承っておりますので、お気軽にご相談ください。</p>
    <a class="btn" href="#">会社概要はこちら<svg width="16" height="8" viewBox="0 0 16 8"><path d="M0 4h15M11 1l4 3-4 3" fill="none" stroke="#fff"/></svg></a>
  </div>
</section>

<section class="service">
  <div class="ghost">SERVICE</div>
  <div class="service-head"><h2 class="sec-title">事業内容</h2><div class="sec-sub">SERVICE</div></div>
  <div class="service-panels">
    <div class="panel panel-1">
      <div class="panel-photo" role="img" aria-label="工場内の掘削製品の写真"></div>
      <div class="panel-body">
        <h3>掘削製品</h3><div class="sec-sub">CUTTING PRODUCTS</div>
        <p>掘削製品の設計から制作、<br>改造まで現場に合わせて一貫対応します。</p>
        <a class="btn" href="#">詳しくはこちら<svg width="14" height="8" viewBox="0 0 14 8"><path d="M0 4h13M9 1l4 3-4 3" fill="none" stroke="#fff"/></svg></a>
      </div>
    </div>
    <div class="panel panel-2">
      <div class="panel-photo" role="img" aria-label="屋外に並ぶ中古くい打ち機の写真"></div>
      <div class="panel-body">
        <h3>くい打ち機中古販売</h3><div class="sec-sub">USED SALE</div>
        <p>メンテナンス済みの良質な<br>くい打ち機を中古でご提供します。</p>
        <a class="btn" href="#">詳しくはこちら<svg width="14" height="8" viewBox="0 0 14 8"><path d="M0 4h13M9 1l4 3-4 3" fill="none" stroke="#fff"/></svg></a>
      </div>
    </div>
  </div>
</section>

<section class="products">
  <div class="ghost">PRODUCT</div>
  <div class="products-head"><h2 class="sec-title">製品例</h2><div class="sec-sub">PRODUCT EXAMPLE</div></div>
  <div class="product-list">
    <div class="product"><div class="product-photo" role="img" aria-label="オーガーヘッドの製品写真"></div><span>オーガーヘッド</span></div>
    <div class="product"><div class="product-photo" role="img" aria-label="ビットの製品写真"></div><span>ビット</span></div>
    <div class="product"><div class="product-photo" role="img" aria-label="スクリューの製品写真"></div><span>スクリュー</span></div>
    <div class="product"><div class="product-photo" role="img" aria-label="一般掘削金具の製品写真"></div><span>一般掘削金具</span></div>
  </div>
  <a class="btn" href="#">製品例一覧はこちら<svg width="16" height="8" viewBox="0 0 16 8"><path d="M0 4h15M11 1l4 3-4 3" fill="none" stroke="#fff"/></svg></a>
</section>

<section class="contact">
  <div class="ghost">CONTACT</div>
  <div class="contact-head"><h2 class="sec-title">お問い合わせ</h2><div class="sec-sub">CONTACT</div></div>
  <p class="contact-note">お見積もり・お問い合わせはこちらまで</p>
  <div class="contact-row">
    <div class="tel">
      <svg width="30" height="30" viewBox="0 0 30 30"><rect width="30" height="30" fill="#1f4fa6"/><path d="M10 7l3 4-2 2c1 2.5 3.5 5 6 6l2-2 4 3-2 3c-6 0-14-8-14-14z" fill="#fff"/></svg>
      000-000-0000
    </div>
    <a class="btn" href="#"><svg width="18" height="13" viewBox="0 0 18 13"><rect x=".5" y=".5" width="17" height="12" fill="none" stroke="#fff"/><path d="M1 1l8 6 8-6" fill="none" stroke="#fff"/></svg>メールでのお問い合わせ</a>
  </div>
</section>

<footer class="site-footer">
  <div class="brand">株式会社○○○○</div>
  <p class="f-address">〒000-0000　○○県○○市○○町0-0<br>TEL 000-000-0000　FAX 000-000-0000</p>
  <nav class="f-nav"><span>ホーム</span><span>会社概要</span><span>事業内容</span><span>製品紹介</span><span>お問い合わせ</span></nav>
  <p class="copy">© 株式会社○○○○ All Rights Reserved.</p>
</footer>

</body>
</html>
```